Business Card Design Project

We are looking for a new business card design for a Drilling company in WA, Australia.

We are in between offices, however require a design in the meantime due to some upcoming events with our basic information.

The Logo for our company is Blue and Grey and would like this colour scheme throughout.

We are quite a new company so would like a memorable design that stands out and communicates a strong commitment to safety, quality of work and performance.

The company name is Ridgeback Boring Works (RBW)

The details to be included are as follows:

Martin Calloway
Managing Director
m.0481639027
e.martin@rbwgroup.com.au

Simon Calloway
Director
m.0429561384
e.simon@rbwgroup.com.au

Industry/Entity Type

Events

Requirements
Must have
• Under the Logo, we would like 'Western Australia'

```html
<!DOCTYPE html>
<html lang="en">
<head>
<meta charset="utf-8">
<title>Ridgeback Boring Works — Business Card</title>
<link href="https://fonts.googleapis.com/css2?family=Arimo:wght@400;700&display=swap" rel="stylesheet">
<style>
  :root {
    --page-bg: #ecebe8;
    --card-bg: #ffffff;
    --brand-blue: #0d3f8f;
    --brand-grey: #6f6f72;
    --card-shadow: rgba(0, 0, 0, 0.18);
  }
  html, body {
    margin: 0;
    padding: 0;
    width: 1200px;
    height: 1000px;
    overflow: hidden;
    background: var(--page-bg);
    font-family: "Arimo", Arial, sans-serif;
  }
  .card-set {
    position: absolute;
    top: 345px;
    left: 50px;
    display: flex;
    gap: 20px;
  }
  .card {
    width: 540px;
    height: 310px;
    background: var(--card-bg);
    box-shadow: 0 4px 14px var(--card-shadow);
  }
  .card svg { display: block; }
  .rule { stroke: var(--brand-blue); stroke-width: 5; fill: none; stroke-linejoin: round; }
  .brand-name { fill: var(--brand-blue); font-weight: 700; font-size: 22px; font-family: "Arimo", Arial, sans-serif; }
  .brand-region { fill: var(--brand-grey); font-size: 12px; letter-spacing: 1px; font-family: "Arimo", Arial, sans-serif; }
  .person-name { fill: var(--brand-blue); font-weight: 700; font-size: 15px; font-family: "Arimo", Arial, sans-serif; }
  .person-title { fill: var(--brand-grey); font-size: 12px; font-family: "Arimo", Arial, sans-serif; }
  .person-contact { fill: var(--brand-blue); font-size: 13px; font-family: "Arimo", Arial, sans-serif; }
</style>
</head>
<body>
  <main class="card-set">
    <section class="card card-front" aria-label="Card front">
      <svg width="540" height="310" viewBox="0 0 540 310">
        <polyline class="rule" points="80,200 360,200 540,172"/>
        <text class="brand-name" x="80" y="188">Ridgeback Boring Works</text>
        <text class="brand-region" x="80" y="222">WESTERN AUSTRALIA</text>
      </svg>
    </section>
    <section class="card card-back" aria-label="Card back">
      <svg width="540" height="310" viewBox="0 0 540 310">
        <polyline class="rule" points="0,198 200,198 360,110 540,110"/>
        <g class="contact contact-martin">
          <text class="person-name" x="60" y="190">Martin Calloway</text>
          <text class="person-title" x="75" y="218">Managing Director</text>
          <text class="person-contact" x="75" y="248">0481639027</text>
          <text class="person-contact" x="75" y="266">martin@rbwgroup.com.au</text>
        </g>
        <g class="contact contact-simon" text-anchor="end">
          <text class="person-name" x="505" y="102">Simon Calloway</text>
          <text class="person-title" x="505" y="130">Director</text>
          <text class="person-contact" x="505" y="160">0429561384</text>
          <text class="person-contact" x="505" y="178">simon@rbwgroup.com.au</text>
        </g>
      </svg>
    </section>
  </main>
</body>
</html>
```